New Business Cards for KM&DR

We need updated business cards for a staff of 15 engineers, estimators, project managers, and sales people. We have recently begun changes to our website and marketing material to improve our look and branding. We are an established fabricator specializing in pressure vessels, tanks, and structural steel. The owners require us to use the existing logo and old english text design. Also, we prefer dark grey or mostly black cards.
Target Market(s)
Engineers, purchasing agents, estimators, and project managers of; mining companies, refineries, industrial construction professionals
Industry/Entity Type
Business
Contact Information for Business Card
Logo, phone, website, email, etc.
Look and feel
Each slider illustrates characteristics of the customer's brand and the style your logo design should communicate.

```html
<!DOCTYPE html>
<html lang="en">
<head>
<meta charset="utf-8">
<title>KM&amp;DR Business Cards</title>
<link href="https://fonts.googleapis.com/css2?family=Roboto:wght@400;500&family=Libre+Baskerville:wght@700&family=UnifrakturMaguntia&display=swap" rel="stylesheet">
<style>
  :root {
    --page-bg: #e4e2df;
    --card-white: #f3f3f3;
    --ink-black: #1f1d1e;
    --band-grey: #a9a9a9;
    --text-white: #ffffff;
    --text-dark: #1f1d1e;
    --url-grey: #4a4a4a;
  }
  html, body {
    margin: 0;
    width: 1200px;
    height: 960px;
    overflow: hidden;
    background: var(--page-bg);
  }
  .canvas {
    position: relative;
    width: 1200px;
    height: 960px;
  }
  .card {
    position: absolute;
    width: 600px;
    height: 343px;
    background: var(--card-white);
    box-shadow: 2px 3px 5px rgba(0,0,0,0.35);
    overflow: hidden;
  }
  .card-front { left: 314px; top: 113px; }
  .card-back { left: 311px; top: 471px; height: 344px; }

  .company-title {
    position: absolute;
    top: 50px;
    left: 0;
    width: 100%;
    text-align: center;
    margin: 0;
    font-family: "Libre Baskerville", serif;
    font-weight: 700;
    font-size: 20px;
    color: var(--text-dark);
    letter-spacing: 0.2px;
  }
  .company-title .initial {
    font-family: "UnifrakturMaguntia", serif;
    font-weight: 400;
    font-size: 25px;
  }

  .contact-band {
    position: absolute;
    left: 0;
    top: 128px;
    width: 600px;
    height: 194px;
  }
  .contact-details {
    position: absolute;
    left: 46px;
    top: 149px;
    font-family: "Roboto", sans-serif;
    color: var(--text-white);
  }
  .person-name {
    margin: 0;
    font-weight: 500;
    font-size: 20px;
    line-height: 24px;
  }
  .person-role {
    margin: 1px 0 0;
    font-size: 14px;
    line-height: 18px;
  }
  .address {
    margin: 11px 0 0;
    font-style: normal;
    font-size: 14px;
    line-height: 18px;
  }
  .contact-list {
    list-style: none;
    margin: 8px 0 0;
    padding: 0;
    font-size: 14px;
    line-height: 20px;
  }
  .contact-list li {
    display: flex;
    align-items: center;
    gap: 8px;
  }
  .contact-list svg { width: 13px; height: 13px; fill: var(--text-white); }

  .brand-name {
    position: absolute;
    font-family: "Roboto", sans-serif;
    font-weight: 500;
    margin: 0;
    text-align: center;
  }
  .brand-front {
    left: 330px;
    top: 205px;
    width: 228px;
    font-size: 40px;
    color: var(--text-white);
  }
  .brand-back {
    left: 0;
    top: 148px;
    width: 600px;
    font-size: 46px;
    color: var(--text-dark);
  }
  .site-url {
    position: absolute;
    left: 0;
    top: 292px;
    width: 600px;
    text-align: center;
    margin: 0;
    font-family: "Roboto", sans-serif;
    font-size: 14px;
    letter-spacing: 7px;
    color: var(--url-grey);
  }
</style>
</head>
<body>
<main class="canvas">
  <section class="card card-front" aria-label="Business card front">
    <h1 class="company-title"><span class="initial">K</span>eystone <span class="initial">M</span>etal &amp; <span class="initial">D</span>ome <span class="initial">R</span>igging</h1>

    <svg class="contact-band" viewBox="0 0 600 194" aria-hidden="true">
      <rect x="0" y="0" width="600" height="194" fill="var(--ink-black)"/>
      <polygon points="506,0 600,0 600,194 506,194 560,97" fill="var(--band-grey)"/>
    </svg>

    <div class="contact-details">
      <p class="person-name">EVAN MARSH</p>
      <p class="person-role">CEO/FOUNDER</p>
      <address class="address">48 East 300 South<br>Riverton Falls 84210</address>
      <ul class="contact-list">
        <li>
          <svg viewBox="0 0 16 16" aria-hidden="true"><path d="M3.6 1.2l2.3 2.6-1.3 2a9 9 0 0 0 5.6 5.6l2-1.3 2.6 2.3-1.3 2.4C8 14.8 1.2 8 .8 2.5z"/></svg>
          <span>555.310.4826</span>
        </li>
        <li>
          <svg viewBox="0 0 16 16" aria-hidden="true"><path d="M4 1h8v4H4zM1 6h14v6h-2v-2H3v2H1zM4 11h8v4H4z"/></svg>
          <span>555.310.7719</span>
        </li>
        <li>
          <svg viewBox="0 0 16 16" aria-hidden="true"><circle cx="8" cy="8" r="7"/><path d="M5 4c2 1 1 3 3 3s1 3 3 2M9 13c0-2 2-2 3-3" stroke="var(--ink-black)" stroke-width="1.2" fill="none"/></svg>
          <span>www.kmanddr.com</span>
        </li>
      </ul>
    </div>

    <p class="brand-name brand-front">KM&amp;DR</p>
  </section>

  <section class="card card-back" aria-label="Business card back">
    <p class="brand-name brand-back">KM&amp;DR</p>
    <p class="site-url">www.kmanddr.com</p>
  </section>
</main>
</body>
</html>
```